Find Bright Harbor Business Card and logo

We need a logo design and business card for a new consulting firm called Find Bright Harbor. We specialize in Digital Transformation of enterprises of all sizes. We help enterprises understand & significantly increase their business velocity. This requires changes in culture, organization, process and technology. We also partner with advanced technology companies to deliver tangible accelerated solutions. Methods utilized include Agile, Design Thinking, Advanced Technology Platforms (microservices, digital data, virtualization, blockchain, etc.). The final design should communicate velocity, transformation, growth and innovation.

Target Market(s)

Large Corporations and Enterprises

Contact Information for Business Card

Tagline - Shape the Coming

Logo Text

Find Bright Harbor or an initial or initials or a symbol/picture

Requirements
Must have
• Front side: Logo, name of business (Find Bright Harbor), tagline (Shape the Coming)
• Back side: First Name, Last Name, Title, Mobile Phone, Email, LinkedIn, URL (findbrightharbor.com)
Nice to have
• The design should communicate velocity, transformation, growth and/or innovation.

```html
<!DOCTYPE html>
<html lang="en">
<head>
<meta charset="utf-8">
<title>Find Bright Harbor – Business Card</title>
<link rel="stylesheet" href="https://fonts.googleapis.com/css2?family=Arimo:wght@400;700&family=Dosis:wght@500;600&family=Jost:wght@300&display=swap">
<style>
  :root {
    --navy: #031893;
    --green: #52ff7a;
    --sky: #40c4f7;
    --paper: #ffffff;
  }
  html, body {
    margin: 0;
    width: 1200px;
    height: 1200px;
    overflow: hidden;
    background: var(--paper);
  }
  .sheet { display: block; width: 1200px; height: 1200px; }
  .card-face { fill: var(--paper); }
  .band-green { fill: var(--green); }
  .band-navy { fill: var(--navy); }
  .band-sky { fill: var(--sky); }
  .brand-dot { fill: var(--navy); }
  .brand-name { font-family: "Arimo", Arial, sans-serif; font-weight: 700; fill: var(--navy); }
  .tagline { font-family: "Dosis", sans-serif; font-weight: 500; font-size: 30px; fill: var(--navy); }
  .view-label { font-family: "Jost", sans-serif; font-weight: 300; font-size: 44px; fill: var(--navy); letter-spacing: 1px; }
  .holder-name { font-family: "Arimo", Arial, sans-serif; font-weight: 400; font-size: 50px; fill: var(--navy); }
  .contact-line { font-family: "Dosis", sans-serif; font-weight: 600; font-size: 28px; fill: var(--navy); letter-spacing: 0.5px; }
  .icon { fill: var(--paper); }
  .icon-stroke { fill: none; stroke: var(--paper); stroke-width: 2.5; }
</style>
</head>
<body>
<svg class="sheet" viewBox="0 0 1500 1500" xmlns="http://www.w3.org/2000/svg">
  <defs>
    <filter id="card-shadow" x="-5%" y="-5%" width="110%" height="115%">
      <feDropShadow dx="0" dy="2" stdDeviation="4" flood-color="#000" flood-opacity="0.18"/>
    </filter>
  </defs>

  <!-- Front of card -->
  <g class="card card--front" transform="translate(232 76)">
    <rect class="card-face" width="1050" height="600" filter="url(#card-shadow)"/>
    <rect class="band-green" width="1050" height="29"/>
    <polygon class="band-sky" points="0,484 560,492 0,508"/>
    <polygon class="band-navy" points="0,508 1050,472 1050,511 0,511"/>
    <rect class="band-green" y="511" width="1050" height="89"/>

    <circle class="brand-dot" cx="513" cy="186" r="62"/>
    <text class="brand-name" x="516" y="337" font-size="56" text-anchor="middle">Find Bright Harbor</text>
    <text class="tagline" x="516" y="414" text-anchor="middle">Shape the Coming</text>
  </g>
  <text class="view-label" x="748" y="751" text-anchor="middle">FRONT VIEW</text>

  <!-- Back of card -->
  <g class="card card--back" transform="translate(228 811)">
    <rect class="card-face" width="1050" height="600" filter="url(#card-shadow)"/>
    <polygon class="band-green" points="438,341 477,312 477,489 438,489"/>
    <polygon class="band-navy" points="492,0 531,0 531,441 492,424"/>
    <polygon class="band-sky" points="0,484 560,492 0,508"/>
    <polygon class="band-navy" points="0,508 1050,472 1050,511 0,511"/>
    <rect class="band-green" y="511" width="1050" height="89"/>

    <circle class="brand-dot" cx="235" cy="208" r="58"/>
    <text class="brand-name" x="237" y="338" font-size="40" text-anchor="middle">Find Bright Harbor</text>

    <text class="holder-name" x="972" y="101" text-anchor="end">Your Name</text>

    <!-- contact icons -->
    <g class="icon-title" transform="translate(513 238)">
      <circle class="icon" cx="0" cy="-6" r="6"/>
      <path class="icon" d="M-11 13 Q-11 1 0 1 Q11 1 11 13 Z"/>
    </g>
    <g class="icon-mobile" transform="translate(513 283)">
      <rect class="icon-stroke" x="-7" y="-12" width="14" height="24" rx="2"/>
      <line class="icon-stroke" x1="-3" y1="8" x2="3" y2="8"/>
    </g>
    <g class="icon-email" transform="translate(513 323)">
      <rect class="icon" x="-11" y="-8" width="22" height="16" rx="1"/>
      <path d="M-11 -7 L0 2 L11 -7" fill="none" stroke="var(--navy)" stroke-width="2"/>
    </g>
    <rect class="icon icon-linkedin" x="505" y="355" width="16" height="16"/>
    <g class="icon-web" transform="translate(513 399)">
      <circle class="icon-stroke" r="11"/>
      <ellipse class="icon-stroke" rx="5" ry="11"/>
      <line class="icon-stroke" x1="-11" y1="0" x2="11" y2="0"/>
    </g>

    <text class="contact-line" x="544" y="251">Title</text>
    <text class="contact-line" x="545" y="294">Mobile</text>
    <text class="contact-line" x="545" y="333">Email</text>
    <text class="contact-line" x="550" y="374">LinkedIn</text>
    <text class="contact-line" x="550" y="411">findbrightharbor.com</text>
  </g>
  <text class="view-label" x="748" y="1461" text-anchor="middle">BACK VIEW</text>
</svg>
</body>
</html>
```